Brasko Construction Business Card

I need a business card design for my company.
We are a construction/machinery company.
I would like to see my logo on the front of the card and my details on the other side
I would like the card to be black or dark grey in colour,with my logo as i send it or modified with a lighter blue colour
I would like to see the design kept fairly simple,but eye catching at the same time
Industry/Entity Type
Business
Contact Information for Business Card
Name
Phone Number
Address
Email
Colors
00a990
1b1b1b
000000
474747
ececec

```html
<!DOCTYPE html>
<html lang="en">
<head>
<meta charset="utf-8">
<title>Brasko Construction Business Card</title>
<link href="https://fonts.googleapis.com/css2?family=Open+Sans:wght@400;600;700&display=swap" rel="stylesheet">
<style>
  :root {
    --stage: #d9d6d1;
    --card-top: #2a2b2d;
    --card-bottom: #121314;
    --accent: #3ec6ec;
    --accent-soft: #2a9dc0;
    --text-light: #e6e6e6;
    --text-muted: #a9abad;
  }
  * { margin: 0; padding: 0; box-sizing: border-box; }
  html, body {
    width: 1200px;
    height: 1023px;
    overflow: hidden;
    background: var(--stage);
    font-family: "Open Sans", Arial, sans-serif;
  }
  .stage {
    position: relative;
    width: 1200px;
    height: 1023px;
  }
  .card {
    position: absolute;
    width: 525px;
    height: 300px;
    border-radius: 4px;
    background: linear-gradient(160deg, var(--card-top), var(--card-bottom));
    box-shadow: 0 10px 28px rgba(0,0,0,0.35);
    overflow: hidden;
  }
  .card--details { left: 50px; top: 362px; }
  .card--brand { left: 625px; top: 362px; }

  /* contact side */
  .brand-mark {
    position: absolute;
    left: 36px;
    top: 34px;
    display: flex;
    align-items: center;
    gap: 12px;
    color: var(--accent);
    font-weight: 700;
    line-height: 1;
  }
  .brand-mark__square {
    width: 30px;
    height: 30px;
    background: var(--accent);
  }
  .brand-mark__name { font-size: 20px; letter-spacing: 1px; text-transform: uppercase; }

  .person {
    position: absolute;
    left: 36px;
    top: 118px;
  }
  .person__name {
    color: var(--accent);
    font-weight: 600;
    font-size: 16px;
    letter-spacing: 0.5px;
    text-transform: uppercase;
  }
  .person__title {
    color: var(--text-muted);
    font-size: 12px;
    margin-top: 2px;
  }
  .rule {
    position: absolute;
    left: 36px;
    top: 170px;
    width: 230px;
    height: 1px;
    background: linear-gradient(90deg, var(--accent), rgba(62,198,236,0));
  }
  .contact-list {
    position: absolute;
    left: 36px;
    top: 186px;
    list-style: none;
  }
  .contact-list li,
  .address li {
    display: flex;
    align-items: center;
    gap: 8px;
    color: var(--text-light);
    font-size: 12.5px;
    line-height: 22px;
    white-space: nowrap;
  }
  .icon { width: 11px; height: 11px; flex: none; }

  .divider {
    position: absolute;
    left: 318px;
    top: 90px;
    width: 1px;
    height: 180px;
    background: linear-gradient(180deg, rgba(62,198,236,0), var(--accent-soft) 30%, var(--accent-soft) 70%, rgba(62,198,236,0));
  }
  .address {
    position: absolute;
    left: 340px;
    top: 110px;
    list-style: none;
  }

  /* logo side */
  .card--brand .brand-block {
    position: absolute;
    inset: 0;
    display: flex;
    align-items: center;
    justify-content: center;
    gap: 16px;
    color: var(--accent);
    font-weight: 700;
  }
  .brand-block__square {
    width: 46px;
    height: 46px;
    background: var(--accent);
  }
  .brand-block__name {
    font-size: 34px;
    letter-spacing: 2px;
    text-transform: uppercase;
    line-height: 1.05;
  }
</style>
</head>
<body>
<main class="stage">

  <section class="card card--details" aria-label="Business card, contact side">
    <div class="brand-mark">
      <span class="brand-mark__square"></span>
      <span class="brand-mark__name">Brasko Construction</span>
    </div>

    <div class="person">
      <p class="person__name">Dr. Marten Lask</p>
      <p class="person__title">Head Scientist</p>
    </div>

    <div class="rule"></div>

    <ul class="contact-list">
      <li>
        <svg class="icon" viewBox="0 0 12 12"><rect width="12" height="12" rx="2" fill="#3ec6ec"/><path d="M3.5 3h1.6l.6 1.8-.9.7a4.5 4.5 0 0 0 1.7 1.7l.7-.9 1.8.6v1.6A5.5 5.5 0 0 1 3.5 3z" fill="#1a1b1c"/></svg>
        +372 5100 4821
      </li>
      <li>
        <svg class="icon" viewBox="0 0 12 12"><rect width="12" height="12" rx="2" fill="#3ec6ec"/><rect x="3" y="2.5" width="6" height="7" rx="1" fill="#1a1b1c"/></svg>
        +372 5100 4836
      </li>
      <li>
        <svg class="icon" viewBox="0 0 12 12"><rect width="12" height="12" rx="2" fill="#3ec6ec"/><path d="M2.5 4h7v4.5h-7z M2.5 4l3.5 2.6L9.5 4" fill="none" stroke="#1a1b1c" stroke-width="1"/></svg>
        marten.lask@braskobuild.com
      </li>
    </ul>

    <div class="divider"></div>

    <ul class="address">
      <li>14 Quarry Lane, 40512</li>
      <li>Millbrook, Estonia</li>
      <li>
        <svg class="icon" viewBox="0 0 12 12"><rect width="12" height="12" rx="2" fill="#3ec6ec"/><circle cx="6" cy="6" r="3.2" fill="none" stroke="#1a1b1c" stroke-width="1"/><path d="M2.8 6h6.4" stroke="#1a1b1c" stroke-width="1"/></svg>
        www.braskobuild.com
      </li>
    </ul>
  </section>

  <section class="card card--brand" aria-label="Business card, logo side">
    <div class="brand-block">
      <span class="brand-block__square"></span>
      <span class="brand-block__name">Brasko<br>Construction</span>
    </div>
  </section>

</main>
</body>
</html>
```